The Book Cover for "Embracing the Quiet Lantern of Dawn" needs redesigned

First the back ground or art work needs to be replaced or redesigned.
The title Embracing the Quiet Lantern of Dawn needs to be redesigned so that the words "Discovering the" is diminished in size compared to the rest of the title "Quiet Lantern of Dawn"
The Sub-title "Tracing the silent journey of the Wandering Flame" needs to be more pronounced and readable.
The authors name needs to be downsized.

```html
<!DOCTYPE html>
<html lang="en">
<head>
<meta charset="utf-8">
<title>Embracing the Quiet Lantern of Dawn — Book Cover</title>
<link rel="stylesheet" href="https://fonts.googleapis.com/css2?family=Poppins:wght@300;400;600;700;800&family=Great+Vibes&display=swap">
<style>
  :root {
    --stage: #5d8790;
    --navy: #1f1b55;
    --ink-script: #1d1a5c;
    --gold: #f6ae22;
    --white: #ffffff;
    --sky-top: #2a3238;
    --sky-mid: #8a94a6;
    --sky-light: #d9d6da;
    --field-blue: #3e86b8;
    --field-green: #3f6a4a;
  }
  * { margin: 0; padding: 0; box-sizing: border-box; }
  html, body {
    width: 1200px; height: 792px; overflow: hidden;
    background: var(--stage);
  }
  .stage {
    width: 1200px; height: 792px;
    display: flex; align-items: center; justify-content: center;
  }
  .cover {
    position: relative;
    width: 520px; height: 762px;
    background: var(--navy);
    overflow: hidden;
    font-family: "Poppins", sans-serif;
    color: var(--white);
  }
  .sky-art {
    position: absolute; left: 0; top: 0; width: 100%; height: 310px;
    background: linear-gradient(180deg, var(--sky-top) 0%, #4a5560 22%, var(--sky-mid) 45%, var(--sky-light) 58%, #6f6f98 78%, var(--navy) 100%);
  }
  .meadow-art {
    position: absolute; left: 36px; top: 258px; width: 443px; height: 432px;
    border-radius: 46% 52% 30% 34% / 30% 34% 40% 44%;
    background: linear-gradient(180deg, #c9cde0 0%, var(--field-blue) 22%, #2f6f8e 36%, var(--field-green) 52%, #3a5a52 72%, rgba(31,27,85,0.9) 100%);
    opacity: 0.92;
  }
  .meadow-fade {
    position: absolute; left: 0; top: 520px; width: 100%; height: 180px;
    background: linear-gradient(180deg, rgba(31,27,85,0) 0%, var(--navy) 90%);
  }
  .title-block { position: absolute; left: 0; top: 0; width: 100%; height: 240px; font-weight: 400; }
  .title-block > span { position: absolute; line-height: 1; white-space: nowrap; }
  .title-lead {
    top: 53px; left: 76px; width: 303px;
    display: flex; align-items: center; gap: 8px;
    font-size: 24px; font-weight: 700; color: var(--gold);
  }
  .title-lead .rule { flex: 1; height: 1px; background: var(--gold); }
  .title-main { top: 74px; left: 72px; font-size: 76px; font-weight: 700; letter-spacing: -1px; }
  .title-mid { top: 140px; left: 76px; font-size: 38px; }
  .title-script {
    top: 112px; left: 282px;
    font-family: "Great Vibes", cursive;
    font-size: 80px; color: var(--ink-script);
  }
  .subtitle { position: absolute; left: 0; top: 0; width: 100%; height: 100%; font-weight: 400; }
  .subtitle > span {
    position: absolute; left: 0; width: 100%;
    text-align: center; line-height: 1; white-space: nowrap;
  }
  .subtitle-lead { top: 542px; font-size: 34px; font-weight: 700; letter-spacing: 12px; padding-left: 12px; }
  .subtitle-mid { top: 577px; font-size: 26px; }
  .subtitle-main { top: 605px; font-size: 48px; font-weight: 700; color: var(--gold); }
  .author {
    position: absolute; left: 0; top: 696px; width: 100%;
    text-align: center; font-size: 17px; font-weight: 400; line-height: 1;
  }
</style>
</head>
<body>
<main class="stage">
  <article class="cover">
    <div class="sky-art" role="img" aria-label="Photograph of a dusky cloudy sky over a grassy hill with a silhouetted mother lifting a child"></div>
    <div class="meadow-art" role="img" aria-label="Photograph of a girl running with open arms through a summer meadow, framed in a silhouette cut-out"></div>
    <div class="meadow-fade"></div>

    <h1 class="title-block">
      <span class="title-lead"><span class="rule"></span>EMBRACING THE<span class="rule"></span></span>
      <span class="title-main">QUIET</span>
      <span class="title-mid">LANTERN OF</span>
      <span class="title-script">Dawn</span>
    </h1>

    <h2 class="subtitle">
      <span class="subtitle-lead">TRACING</span>
      <span class="subtitle-mid">THE SILENT JOURNEY OF THE</span>
      <span class="subtitle-main">WANDERING FLAME</span>
    </h2>

    <p class="author">R T Finch Halloway</p>
  </article>
</main>
</body>
</html>
```